Fast Business Card Project

I need a business card with the name RENATO COSTA stylized on one side and my email on the other (renatolima4711@mailbrisa.com)

Industry/Entity Type

Business

Contact Information for Business Card

www.trilvento.com.br

```html
<!DOCTYPE html>
<html lang="pt-BR">
<head>
<meta charset="UTF-8">
<title>Renato Costa — Cartão de Visita</title>
<link rel="stylesheet" href="https://fonts.googleapis.com/css2?family=Arimo:wght@700&display=swap">
<style>
  :root {
    --ink: #000000;
    --paper: #ffffff;
    --name-grey: #dcdcdc;
    --edge-grey: #8a8a8a;
  }
  html, body {
    margin: 0;
    padding: 0;
    overflow: hidden;
    background: var(--paper);
  }
  .card {
    position: relative;
    width: 1200px;
    height: 686px;
    overflow: hidden;
    background: var(--paper);
  }
  .card__field {
    position: absolute;
    left: 0;
    top: 0;
    width: 1200px;
    height: 580px;
    background: var(--ink);
  }
  .card__stripe {
    position: absolute;
    left: 0;
    width: 1200px;
    background: var(--ink);
  }
  .card__stripe--lower {
    top: 590px;
    height: 12px;
  }
  .card__edge {
    position: absolute;
    left: 0;
    top: 684px;
    width: 1200px;
    height: 2px;
    background: var(--edge-grey);
  }
  .card__name {
    position: absolute;
    left: 108px;
    top: 82px;
    margin: 0;
    font-family: "Arimo", Arial, sans-serif;
    font-weight: 700;
    font-size: 47px;
    line-height: 1;
    letter-spacing: 24px;
    color: var(--name-grey);
    white-space: nowrap;
  }
  .card__name .word-gap {
    display: inline-block;
    width: 22px;
  }
</style>
</head>
<body>
  <main class="card">
    <div class="card__field"></div>
    <div class="card__stripe card__stripe--lower"></div>
    <div class="card__edge"></div>
    <h1 class="card__name">RENATO<span class="word-gap"></span> COSTA</h1>
  </main>
</body>
</html>
```